In Home Personal IT Consultant (Nerd) Website and Logo QTgeek.net

Website and logo design for in home personal "nerd". Consulting services provided: Home Automation, Home Theater, Network and Wi-Fi installation, Computer Repair, and Virus Removal. Need simple site to promote QTgeek.net based in Santa Fe, New Mexico. You may choose to incorporate the Zia symbol from the New Mexico flag into the design, not mandatory. I am also a big fan of the movie Return of the Tinkers.
I have over 10 years of experience in the hospitality industry working with multi million dollar hotels and will apply that same level of service to the home. TechVara B+ and Shieldwise+ Certified. Available by appointment, primarily Evenings and Weekends. Consulting rate will be $70/hr.
Industry/Entity Type
Consulting
Number of Pages Required
1 page
Look and feel
Each slider illustrates characteristics of the customer's brand and the style your logo design should communicate.

```html
<!DOCTYPE html>
<html lang="en">
<head>
<meta charset="utf-8">
<title>QT Geek — In Home IT Personal Consultant</title>
<link href="https://fonts.googleapis.com/css2?family=Open+Sans:wght@400;600;700&display=swap" rel="stylesheet">
<style>
  :root {
    --red: #c8202a;
    --red-dark: #5c0508;
    --red-mid: #a8121b;
    --ink: #333333;
    --muted: #666666;
    --white: #ffffff;
    --card: #f2f2f2;
    --footer: #3a3a3a;
    --footer-text: #cfcfcf;
    --button: #2e2e2e;
  }
  * { box-sizing: border-box; margin: 0; padding: 0; }
  html, body { width: 1200px; height: 2270px; overflow: hidden; }
  body {
    position: relative;
    background: var(--white);
    font-family: "Open Sans", Arial, sans-serif;
    color: var(--ink);
  }

  /* Header */
  .site-header { position: absolute; left: 0; top: 0; width: 1200px; height: 117px; background: var(--white); }
  .brand { position: absolute; left: 132px; top: 46px; display: flex; align-items: center; gap: 10px; }
  .brand-mark { width: 14px; height: 14px; background: var(--red); border-radius: 50%; }
  .brand-name { font-size: 36px; font-weight: 600; color: var(--red); line-height: 1; letter-spacing: -0.5px; }
  .main-nav { position: absolute; top: 66px; left: 698px; display: flex; gap: 0; }
  .main-nav a { position: absolute; font-size: 15px; color: var(--muted); text-decoration: none; white-space: nowrap; }
  .main-nav a.is-active { color: var(--red); }

  /* Hero */
  .hero { position: absolute; left: 0; top: 117px; width: 1200px; height: 497px; }
  .hero-photo {
    position: absolute; inset: 0;
    background: linear-gradient(100deg, #e7ebef 0%, #cfd5dc 35%, #b9c0c8 55%, #dde2e7 75%, #eef1f4 100%);
  }
  .hero-copy { position: absolute; left: 698px; top: 76px; }
  .hero-kicker { font-size: 14px; color: var(--ink); text-transform: uppercase; letter-spacing: 0.3px; }
  .hero-title { font-size: 32px; font-weight: 600; color: var(--ink); margin-top: 2px; letter-spacing: -0.3px; }
  .cert-badge { position: absolute; top: 139px; width: 177px; height: 107px; background: var(--white); border-radius: 3px; }
  .cert-badge--one { left: 1px; }
  .cert-badge--two { left: 192px; }
  .cert-badge .seal { position: absolute; left: 20px; top: 20px; width: 90px; height: 66px; border: 4px solid var(--red); }
  .cert-badge .seal-side { position: absolute; left: 130px; top: 40px; width: 28px; height: 28px; border-radius: 50%; background: #cccccc; }
  .slider-arrow { position: absolute; top: 324px; width: 36px; height: 36px; }

  /* Services */
  .services { position: absolute; left: 0; top: 614px; width: 1200px; height: 385px; }
  .section-title { position: absolute; width: 1200px; text-align: center; font-size: 32px; font-weight: 400; color: var(--red); }
  .services .section-title { top: 70px; }
  .service-tile {
    position: absolute; top: 136px; width: 168px; height: 167px;
    background: var(--red); border-radius: 3px; color: var(--white);
    text-align: center;
  }
  .service-tile svg { position: absolute; left: 62px; top: 20px; width: 44px; height: 44px; }
  .service-tile .label { position: absolute; left: 0; right: 0; top: 78px; font-size: 20px; font-weight: 600; line-height: 26px; }

  /* Booking */
  .booking {
    position: absolute; left: 0; top: 999px; width: 1200px; height: 487px;
    background: radial-gradient(ellipse at 50% 40%, var(--red-mid) 0%, #86080f 45%, var(--red-dark) 100%);
    color: var(--white); text-align: center;
  }
  .booking-lead { position: absolute; top: 64px; width: 1200px; font-size: 31px; font-weight: 400; }
  .booking-sub { position: absolute; top: 104px; width: 1200px; font-size: 23px; }
  .rate-box {
    position: absolute; left: 357px; top: 151px; width: 484px; height: 60px;
    border: 3px solid var(--white); font-size: 25px; font-weight: 700;
    line-height: 54px; text-transform: uppercase; letter-spacing: 0.3px;
  }
  .field {
    position: absolute; height: 40px; background: var(--white);
    font-size: 11px; color: #555; text-align: left; padding: 13px 15px; line-height: 14px;
  }
  .field--select svg { position: absolute; right: 15px; top: 17px; }
  .submit-button {
    position: absolute; left: 560px; top: 375px; width: 80px; height: 39px;
    background: var(--button); color: var(--white); font-size: 12px; font-weight: 700;
    line-height: 39px; border-radius: 2px;
  }

  /* Blog */
  .blog { position: absolute; left: 0; top: 1486px; width: 1200px; height: 687px; }
  .blog .section-title { top: 72px; }
  .blog-card { position: absolute; top: 144px; width: 444px; height: 464px; background: var(--card); }
  .blog-card--one { left: 132px; }
  .blog-card--two { left: 622px; }
  .blog-image { width: 444px; height: 319px; }
  .blog-image--mobile { background: linear-gradient(135deg, #3c6f9a 0%, #8fb8d8 45%, #d9e6ef 100%); }
  .blog-image--security { background: linear-gradient(135deg, #0d2a44 0%, #1f5a82 50%, #0a1f33 100%); }
  .blog-excerpt { padding: 21px 22px 0; font-size: 16px; line-height: 24px; text-align: center; color: var(--ink); }
  .read-more { display: block; margin-top: 9px; text-align: center; font-size: 11px; color: var(--muted); text-decoration: underline; }
  .carousel-arrow { position: absolute; top: 366px; width: 20px; height: 30px; }

  /* Footer */
  .site-footer { position: absolute; left: 0; top: 2173px; width: 1200px; height: 97px; background: var(--footer); color: var(--footer-text); }
  .footer-nav { position: absolute; left: 132px; top: 24px; font-size: 11px; }
  .footer-nav span { margin: 0 6px; }
  .copyright { position: absolute; left: 132px; top: 56px; font-size: 11px; }
  .social-links { position: absolute; left: 908px; top: 36px; display: flex; gap: 9px; }
  .social-links span { width: 25px; height: 25px; border-radius: 50%; display: block; }
</style>
</head>
<body>

<header class="site-header">
  <div class="brand"><span class="brand-name">QT Geek</span><span class="brand-mark"></span></div>
  <nav class="main-nav">
    <a class="is-active" style="left:0">Home</a>
    <a style="left:78px">About</a>
    <a style="left:157px">Services</a>
    <a style="left:249px">Blog</a>
    <a style="left:316px">Contact</a>
  </nav>
</header>

<section class="hero">
  <div class="hero-photo" role="img" aria-label="Photo of a smiling consultant using a tablet at a bright home desk with a laptop and coffee cup"></div>
  <div class="hero-copy">
    <p class="hero-kicker">I'm an inhome</p>
    <h1 class="hero-title">IT Personal Consultant.</h1>
    <div class="cert-badge cert-badge--one" role="img" aria-label="TechVara B+ certification badge"><span class="seal"></span><span class="seal-side"></span></div>
    <div class="cert-badge cert-badge--two" role="img" aria-label="Shieldwise+ certification badge"><span class="seal"></span><span class="seal-side"></span></div>
  </div>
  <svg class="slider-arrow" style="left:44px" viewBox="0 0 36 36"><rect x="5" y="5" width="26" height="26" transform="rotate(45 18 18)" fill="#c8202a" opacity="0.9"/><path d="M21 11 L14 18 L21 25" stroke="#fff" stroke-width="3" fill="none"/></svg>
  <svg class="slider-arrow" style="left:1120px" viewBox="0 0 36 36"><rect x="5" y="5" width="26" height="26" transform="rotate(45 18 18)" fill="#c8202a" opacity="0.9"/><path d="M15 11 L22 18 L15 25" stroke="#fff" stroke-width="3" fill="none"/></svg>
</section>

<section class="services">
  <h2 class="section-title">Consulting services for…</h2>
  <div class="service-tile" style="left:132px">
    <svg viewBox="0 0 44 44" fill="#fff"><circle cx="17" cy="24" r="10"/><circle cx="17" cy="24" r="4" fill="#c8202a"/><g stroke="#fff" stroke-width="4"><path d="M17 10v28M3 24h28M7 14l20 20M27 14 7 34"/></g><circle cx="17" cy="24" r="4" fill="#c8202a"/><circle cx="34" cy="12" r="6"/><circle cx="34" cy="12" r="2.5" fill="#c8202a"/><circle cx="35" cy="32" r="5"/><circle cx="35" cy="32" r="2" fill="#c8202a"/></svg>
    <p class="label">Home<br>Automation</p>
  </div>
  <div class="service-tile" style="left:324px">
    <svg viewBox="0 0 44 44" fill="#fff"><rect x="2" y="10" width="28" height="24" rx="5"/><path d="M31 20 L42 12 V32 L31 24Z"/></svg>
    <p class="label">Home<br>Theater</p>
  </div>
  <div class="service-tile" style="left:516px">
    <svg viewBox="0 0 44 44" fill="none" stroke="#fff" stroke-width="4" stroke-linecap="round"><path d="M3 16 Q22 0 41 16"/><path d="M10 23 Q22 12 34 23"/><path d="M16 30 Q22 25 28 30"/><circle cx="22" cy="37" r="2.5" fill="#fff"/></svg>
    <p class="label">Network and<br>Wi-Fi<br>installation</p>
  </div>
  <div class="service-tile" style="left:708px">
    <svg viewBox="0 0 44 44" fill="#fff"><rect x="2" y="6" width="40" height="26" rx="2"/><rect x="6" y="10" width="32" height="16" fill="#c8202a"/><rect x="18" y="32" width="8" height="5"/><rect x="12" y="37" width="20" height="3"/></svg>
    <p class="label">Computer<br>Repair</p>
  </div>
  <div class="service-tile" style="left:900px">
    <svg viewBox="0 0 44 44" fill="#fff"><path d="M8 6 H36 V24 Q36 36 22 42 Q8 36 8 24Z"/><path d="M22 10 H32 V24 Q32 32 22 37Z" fill="#c8202a"/></svg>
    <p class="label">Virus<br>Removal</p>
  </div>
</section>

<section class="booking" role="region" aria-label="Book an appointment">
  <p class="booking-lead">Available by appointment,</p>
  <p class="booking-sub">primarily Evenings and Weekends.</p>
  <div class="rate-box">Consulting rate will be $70/hr</div>
  <div class="field" style="left:132px;top:246px;width:217px">Name</div>
  <div class="field" style="left:371px;top:246px;width:218px">Email</div>
  <div class="field" style="left:610px;top:246px;width:218px">Phone</div>
  <div class="field field--select" style="left:849px;top:246px;width:218px">Consulting for
    <svg width="10" height="6" viewBox="0 0 10 6"><path d="M0 0H10L5 6Z" fill="#333"/></svg>
  </div>
  <div class="field" style="left:132px;top:310px;width:935px">Messages</div>
  <div class="submit-button">SUBMIT</div>
</section>

<section class="blog">
  <h2 class="section-title">Blog</h2>
  <svg class="carousel-arrow" style="left:46px" viewBox="0 0 20 30"><path d="M15 4 L5 15 L15 26" stroke="#aaa" stroke-width="2" fill="none"/></svg>
  <svg class="carousel-arrow" style="left:1134px" viewBox="0 0 20 30"><path d="M5 4 L15 15 L5 26" stroke="#aaa" stroke-width="2" fill="none"/></svg>
  <article class="blog-card blog-card--one">
    <div class="blog-image blog-image--mobile" role="img" aria-label="Hand holding a smartphone with glowing app tiles floating above it"></div>
    <p class="blog-excerpt">Pellentesque blandit lacus eget nunc faucibus, et tinci-dunt eros viverra. Phasellus consequat sagittis nisi suscipit feugia</p>
    <a class="read-more">Read more</a>
  </article>
  <article class="blog-card blog-card--two">
    <div class="blog-image blog-image--security" role="img" aria-label="Hooded figure behind a blue screen of code, illustrating online security"></div>
    <p class="blog-excerpt">Etiam mattis augue vehicula odio posuere, sit amet tempus lectus luctus. Nulla facilisi. Etiam vel massa elementum, bibendum tellus.</p>
    <a class="read-more">Read more</a>
  </article>
</section>

<footer class="site-footer">
  <nav class="footer-nav">Home<span>|</span>About<span>|</span>Services<span>|</span>Blog<span>|</span>Contact</nav>
  <p class="copyright">Copyright &copy; 2017 QT Geek. All rights reserved.</p>
  <div class="social-links" aria-label="Social links">
    <span style="background:#3b5998"></span>
    <span style="background:#1da1f2"></span>
    <span style="background:#cb2027"></span>
    <span style="background:#e52d27"></span>
    <span style="background:#517fa4"></span>
  </div>
</footer>

</body>
</html>
```